Brindlewort Organic

Please find attached screenshots of a same product as what I'm selling, looking for similar packaging but yet a whole new different design with my own logo plumtiles which is also attached. It will be on white bags with the clear on the bottom center. As far as colors maby green yellow and black or if you have a better idea. Also it needs to be something that looks up to date modern I like when it has that two-tone gloss to it where it goes from darker to lighter.

```html
<!DOCTYPE html>
<html lang="en">
<head>
<meta charset="utf-8">
<title>Brindlewort Organic – plumtiles pouch</title>
<link rel="stylesheet" href="https://fonts.googleapis.com/css2?family=Caprasimo&family=Montserrat:wght@500&family=PT+Sans:wght@700&family=Open+Sans:wght@700&display=swap">
<style>
  :root {
    --backdrop: #1d1d1d;
    --pouch-edge: #0f3a24;
    --pouch-mid: #1c7444;
    --pouch-glow: #2e8c5e;
    --panel: #1f3f2f;
    --panel-edge: #1a3528;
    --slot: #184a30;
    --white: #f2f2f2;
    --gold: #e7c21a;
    --gold-deep: #c9a81b;
    --orange-a: #c9381f;
    --orange-b: #f76a1c;
    --band-green: #1f9a4c;
    --band-yellow: #f1cf1d;
    --ink: #1b1b1b;
    --herb-dark: #5a5234;
    --herb-light: #7d8a4e;
  }
  * { box-sizing: border-box; margin: 0; padding: 0; }
  html, body { width: 1200px; height: 960px; overflow: hidden; }
  body { background: var(--backdrop); position: relative; }

  .pouch {
    position: absolute;
    left: 361px; top: 68px;
    width: 495px; height: 796px;
    border-radius: 22px 22px 0 0;
    background:
      radial-gradient(ellipse 60% 55% at 60% 55%, var(--pouch-glow) 0%, rgba(46,140,94,0) 70%),
      linear-gradient(90deg, var(--pouch-edge) 0%, var(--pouch-mid) 25%, var(--pouch-mid) 75%, var(--pouch-edge) 100%);
    clip-path: polygon(0 0, 100% 0, 100% 90%, 92% 100%, 8% 100%, 0 90%);
    overflow: hidden;
  }
  .pouch::after {
    content: "";
    position: absolute; inset: 0;
    background: linear-gradient(180deg, rgba(0,0,0,0.35) 0%, rgba(0,0,0,0) 35%);
    pointer-events: none;
  }

  .brand-panel {
    position: absolute;
    left: 134px; top: 0;
    width: 250px; height: 294px;
    background: linear-gradient(180deg, var(--panel-edge), var(--panel));
    z-index: 1;
  }
  .hang-slot {
    position: absolute;
    left: 59px; top: 52px;
    width: 126px; height: 19px;
    border-radius: 10px;
    background: var(--slot);
    box-shadow: inset 0 1px 3px rgba(0,0,0,0.5);
  }
  .brand-mark {
    position: absolute;
    left: 93px; top: 142px;
    width: 66px; height: 66px;
    border-radius: 50%;
    border: 4px solid var(--white);
  }
  .brand-name {
    position: absolute;
    left: 0; right: 0; top: 222px;
    text-align: center;
    font-family: "Montserrat", sans-serif;
    font-weight: 500;
    font-size: 27px;
    letter-spacing: 2px;
    color: var(--white);
  }

  .product-title {
    position: absolute;
    left: 0; right: 0; top: 342px;
    text-align: center;
    font-family: "Caprasimo", serif;
    font-size: 43px;
    line-height: 1;
    color: var(--gold);
    background: linear-gradient(90deg, var(--gold-deep), var(--gold));
    -webkit-background-clip: text;
    background-clip: text;
    -webkit-text-fill-color: transparent;
    z-index: 1;
  }
  .title-rule {
    position: absolute;
    left: 84px; top: 416px;
    width: 356px; height: 4px;
    background: var(--white);
    z-index: 1;
  }
  .product-grade {
    position: absolute;
    left: 0; right: 0; top: 432px;
    text-align: center;
    font-family: "PT Sans", sans-serif;
    font-weight: 700;
    font-size: 54px;
    letter-spacing: 4px;
    line-height: 1;
    background: linear-gradient(90deg, var(--orange-a), var(--orange-b));
    -webkit-background-clip: text;
    background-clip: text;
    -webkit-text-fill-color: transparent;
    z-index: 1;
  }

  .product-photo {
    position: absolute;
    left: 65px; top: 514px;
    width: 378px; height: 200px;
    border-radius: 190px 190px 6px 6px;
    background: radial-gradient(ellipse at 50% 35%, var(--herb-dark) 0%, var(--herb-light) 75%, #6f8a45 100%);
    z-index: 1;
  }

  .weight-band {
    position: absolute;
    left: 0; right: 0; top: 711px;
    height: 42px;
    background: var(--band-green);
    display: flex; align-items: center; justify-content: center;
    font-family: "Open Sans", sans-serif;
    font-weight: 700;
    font-size: 21px;
    color: var(--ink);
    z-index: 2;
  }
  .base-band {
    position: absolute;
    left: 0; right: 0; top: 753px;
    height: 43px;
    background: linear-gradient(180deg, #d9b816, var(--band-yellow) 40%, #e9c21a);
    z-index: 2;
  }
</style>
</head>
<body>
  <div class="pouch">
    <div class="brand-panel">
      <div class="hang-slot"></div>
      <div class="brand-mark"></div>
      <div class="brand-name">PLUMTILES</div>
    </div>

    <h1 class="product-title">BRINDLEWORT</h1>
    <div class="title-rule"></div>
    <div class="product-grade">ORGANIC</div>

    <div class="product-photo" role="img" aria-label="Photo of a mound of dried, cut brindlewort leaves"></div>

    <div class="weight-band">Net Wt.&nbsp; 1.27 OZ (36g)</div>
    <div class="base-band"></div>
  </div>
</body>
</html>
```